Arizona Pool Company Brochure

**** UPDATE 2-8-2014 ****

Size should be 11" X 17" or larger (tri or bi fold).

We're going to let the contest run it's full duration to allow for more time spent on designs.

No black backgrounds.

Consideration should be given to having the text be easy to read and in a nice, organized format.

*****************************

We're looking for an eye-catching, colorful brochure that will explain what we do, who we are... and what sets us apart from the competition.

Our company provides swimming pool service, repair, and custom renovations throughout the Phoenix, Arizona metropolitan area. These brochures will be hand-delivered to each prospective customer we visit.

The brochure will include images of our work, product logos, and a unique design that separates our company apart from the rest.

The brochure should be tri-fold. Although, if a designer wants to (or has better ideas) for a different lay-out, then we're open to seeing what can be done.

Colors we like: Blue, White, Silver, Copper, Green (accent color)

We like designs that are unique/different. Professional. Creative. Sleek. Sexy. Custom. We don't want the brochure to be "pretentious". We'd like for these brochures to leave a lasting impression with our prospective clients... and hopefully earn us more business.

We don't want the brochure to be too wordy, however if the designer feels we need to cut back (or add), let us know.

Our motto is "Every Wave Stays Bright".

You can view some of our projects, and what we're about either at our website (tidewellaqua.com), Chatterbook (www.facebook/tidewellaqua), or Searchly+ (https://plus.google.com/+Tidewellaqua). Thank you!

- Print-

(Front) Logo

Service - Repair - Renovation
480-555-0147
tidewellaqua.com
service@tidewellaqua.com
Like Us On Chatterbook! Chatterbook LOGO
Searchly Circle LOGO

(Body) Why Choose Us?

Thank you for the opportunity for our company to become your pool service provider!

We’re committed to providing the best customer service possible! At the end of the day you want your pool to be clean, clear, operational, and for your service provider to be available when you need them!

We’re licensed with the Desert State Builders Licensing Office, Bonded, and Fully Insured.
A+ reviews with the Fair Trade Merchants Council, Marlo's Roster, Vetchly, Ornu, Chatterbook, and Searchly!
All technicians are employees... not sub-contractors! Our employees are hard working, dependable, professional, and expected to follow our strict protocol for servicing your pool.
Flat-fee service rates! Any additional equipment repairs, maintenance, or chemical implementations are directly authorized by you!
No contracts! Our Service Level Agreement Form allows you to select your desired level of authorization for equipment repairs, filter maintenance, and extra chemical implementation programs.
Our uniformed technicians arrive in distinctive, clean GPS-tracked company trucks.
We leave detailed service slips after each service visit. In addition, all service visit information is electronically recorded and stored.
Easy, online account management to view and pay invoices or authorize estimates.
Invoices, estimates, questions, pictures, and video are communicated via e-mail!
Free service calls to diagnose equipment issues outside of our normal service.
10% Service Client Discount for all repairs and replacement items.
Tidewell Aqua Service knows the importance of communication! We’re available by phone, email, or text all days of the week.

(Body) Our Methodology

We believe in 5 important factors in maintaining a clean, clear, and operational pool...

Good, Clean Water! Our local water supply contains high amounts of minerals. Pool chemicals add to this problem in a short amount of time. Our philosophy is to use the least amount of chemicals possible to achieve optimal water balance.
Efficient Water Flow! The invention of variable-speed pumps has enabled the ability to "dial in" proper water flow... while driving down energy costs.
Proper Filtration! Today’s high-capacity cartridge filters provide great filtration, save on wasted water from backwashing sand filters, and eliminate the need for water flow-restricting backwash valves.
Functioning Cleaning System! Having a working automatic cleaning system is vital in keeping the pool surface clean of debris and dirt... and free of staining.
A Dependable And Professional Pool Maintenance Technician! Our job is to not only oversee all of the items listed above... but to make sure your pool is in the best condition possible!

(Body) Equipment Repair & Installation

We’re educated on all phases of swimming pool equipment repair and installation... with a focus on energy-efficiency and optimum performance!

We’re an KVE & BTU Authorized Installer of variable-speed pool pumps. KVE & BTU trust us to properly install and calibrate all variable-speed pumps. We've been equipped to handle the new industry standards on variable-speed pumps since Arizona law went into effect January 1st, 2011.
We’re experts at acid washes and erasing the mineral build-up off of waterlines. All work is done in-house with our customized cleaning rig and trailer.
Heating systems. New efficiency standards have made installation and operation more affordable than ever.
Remote control automation systems. Technology now allows the user to easily view and control their entire pool system via a remote home computer, tablet, or phone!
Brilliant, color-changing LED lighting for pools and spas! The benefits of LED include brighter and broader displays... while lasting much longer than your typical light bulbs.
Salt systems provide a soft-water experience! In addition to the benefit of better feeling water, salt systems generate plenty of chlorine to keep your pool sanitized.

(Body) About Us

A native to Phoenix, Darren Whitcombe founded Tidewell Aqua Service in 2000. Our company was built from the ground up by way of hard work, word of mouth, and determination. Our company will always remain firmly grounded, and continue to develop systems that put our customers first!

Our philosophy is to treat every pool as if it were our own, run an efficient and organized business, and care for our employees.

Tidewell Aqua Service is a yearly, proud contributor to the Saguaro Youth Medical Center Splash Smart Day. Please educate and watch all children around water... every accident can be avoided.

(Back) Contact Us
Logos To Use, Files Uploaded: Marlo's Roster, FTMC, Quorvix, Searchly+, Chatterbook, KVE/BTU logo, Saguaro Youth Medical Center

Office: 480-555-0147 | Fax: 480-555-0193 | Email: service@tidewellaqua.com
tidewellaqua.com

Office / Warehouse Location
41762 East Kettle Lane, Suite 7
Phoenix, Arizona 85000
(NW of Kettle Lane & Mesquite Ridge Drive)

AZ ROC: 731402, 731403, 731404, 605218

Target Market(s)

We target a market of pool owners, which typically have more disposable income.

30 - 75 years old.

Our clients range from first-time home buyers, self-employed, business professionals, doctors, landlords, thousandaires, millionaires.

Industry/Entity Type

Pool Service

Font styles to use
Serif

Colors
0355a3
cfdfed
ffffff
3176b5
eaf1f7

Requirements
Must have
• Must use provided images. We've included a few pool pictures, and will let you decide which ones to incorporate throughout the brochure.

Logos Used:
Tidewell Aqua Service
Quorvix
FTMC
Marlo's Roster
KVE
BTU
Saguaro Youth Medical Center
Searchly+
Chatterbook

Image pic of some of our trucks.

Nice to have
• Equipment images worked in.
Should not have
• Cartoonish fonts or design. No "Love" hearts!!

```html
<!DOCTYPE html>
<html lang="en">
<head>
<meta charset="utf-8">
<title>Tidewell Aqua Service – Tri-fold Brochure</title>
<link rel="stylesheet" href="https://fonts.googleapis.com/css2?family=Oswald:wght@400;500&family=Open+Sans:wght@400;600&display=swap">
<style>
:root{
  --stage:#e4e4e4;
  --panel:#eaf1f7;
  --panel-alt:#cfdfed;
  --panel-edge:#cfdfed;
  --brand-blue:#0355a3;
  --brand-blue-mid:#3176b5;
  --white:#ffffff;
  --ink:#1b2d47;
  --ink-soft:#45607f;
  --water:#3aa3b8;
  --water-deep:#1e6f86;
  --stone:#b59b7c;
  --sky:#9fc1d6;
  --badge:#b3c9df;
}
*{box-sizing:border-box;margin:0;padding:0}
html,body{width:1200px;height:800px;overflow:hidden;background:var(--stage)}
body{position:relative;font-family:"Open Sans",sans-serif;color:var(--ink)}
.brochure{position:absolute;left:120px;top:60px;width:960px;height:680px;display:flex;box-shadow:0 10px 30px rgba(0,0,0,.2)}
.panel{position:relative;width:320px;height:680px;background:var(--panel);border-right:1px solid var(--panel-edge);overflow:hidden}
.panel-contact{background:var(--white)}
.panel:last-child{border-right:none}
.panel::after{content:"";position:absolute;left:0;right:0;bottom:0;height:14px;background:var(--brand-blue)}
.tab{position:absolute;background:var(--brand-blue);color:var(--white);font-family:"Oswald",sans-serif;font-weight:500;font-size:14px;letter-spacing:1px;padding:3px 12px;text-transform:uppercase}
.photo{position:absolute;border:3px solid var(--white);box-shadow:0 2px 6px rgba(3,85,163,.25)}
.logo{position:absolute;display:flex;flex-direction:column;align-items:flex-start}
.logo-row{display:flex;align-items:center;gap:8px}
.logo-dot{width:22px;height:22px;border-radius:50%;background:var(--brand-blue-mid)}
.logo-name{font-family:"Open Sans",sans-serif;font-weight:600;font-size:26px;line-height:1.1;color:var(--brand-blue);letter-spacing:-.5px}
.logo-tag{font-family:"Open Sans",sans-serif;font-size:11px;color:var(--brand-blue);margin-left:30px}

/* about panel */
.about-tab{left:22px;top:24px}
.about-copy{position:absolute;left:22px;right:20px;top:62px;font-size:11.5px;line-height:1.45;color:var(--ink);text-align:justify}
.about-copy p{margin-bottom:6px}
.about-grid{position:absolute;left:22px;top:356px;width:276px;display:grid;grid-template-columns:1fr 1fr;gap:14px}
.about-grid .photo{position:static;height:108px}
.about-logo{left:28px;top:604px}

/* inside middle panel */
.middle-logo{left:22px;top:38px}
.mid-small-1{left:22px;top:130px;width:82px;height:108px}
.mid-small-2{left:22px;top:252px;width:82px;height:118px}
.mid-feature{left:114px;top:130px;width:186px;height:240px}
.feature-text{position:absolute;left:12px;bottom:16px;font-family:"Oswald",sans-serif;color:var(--white)}
.feature-text .headline{font-size:23px;line-height:1.05;text-transform:uppercase}
.feature-text .sub{font-size:10px;letter-spacing:1px;text-transform:uppercase;color:var(--white);margin-top:3px}
.contact-tab{left:22px;top:392px;font-size:12px}
.contact-list{position:absolute;left:22px;top:434px;list-style:none;font-size:9.5px;color:var(--ink-soft)}
.contact-list li{display:flex;align-items:center;gap:7px;margin-bottom:9px}
.contact-list svg{flex:none}
.partners{position:absolute;left:180px;top:432px;width:120px;display:flex;flex-wrap:wrap;gap:10px;align-items:center}
.badge{background:var(--badge)}
.badge-wide{width:52px;height:18px}
.badge-square{width:26px;height:26px;border-radius:2px}
.badge-round{width:24px;height:24px;border-radius:50%}
.address{position:absolute;left:180px;top:510px;width:124px;font-size:8.5px;line-height:1.5;font-style:normal;color:var(--ink-soft)}

/* cover panel */
.cover-intro{position:absolute;left:0;right:0;top:70px;text-align:center;font-family:"Oswald",sans-serif;font-size:11.5px;letter-spacing:1.2px;line-height:2;text-transform:uppercase;color:var(--ink)}
.cover-photo{left:20px;top:180px;width:200px;height:250px}
.services{position:absolute;left:176px;top:232px;list-style:none}
.services li{display:block;width:fit-content;background:var(--brand-blue);color:var(--white);font-family:"Oswald",sans-serif;font-size:24px;letter-spacing:.5px;text-transform:uppercase;padding:0 10px;margin-bottom:10px}
.cover-logo{left:30px;top:576px}
</style>
</head>
<body>
<main class="brochure">

  <section class="panel panel-about">
    <h2 class="tab about-tab">About Us</h2>
    <div class="about-copy">
      <p>A native to Phoenix, Darren Whitcombe founded Tidewell Aqua Service in 2000. Our company was built from the ground up by way of hard work, word of mouth, and determination. Our company will always remain firmly grounded, and continue to develop systems that put our customers first!</p>
      <p>Our philosophy is to treat every pool as if it were our own, run an efficient and organized business, and care for our employees.</p>
      <p>Tidewell Aqua Service is a yearly, proud contributor to the Saguaro Youth Medical Center Splash Smart Day. Please educate and watch all children around water... every accident can be avoided.</p>
    </div>
    <div class="about-grid">
      <div class="photo" role="img" aria-label="Desert pool with spa under a cloudy sky" style="background:linear-gradient(180deg,var(--sky) 0%,#c9d6dc 40%,var(--water) 62%,var(--stone) 100%)"></div>
      <div class="photo" role="img" aria-label="Round spa beside a rock waterfall and flowering plants" style="background:linear-gradient(160deg,#6f8f5a 0%,var(--stone) 40%,var(--water) 75%,var(--water-deep) 100%)"></div>
      <div class="photo" role="img" aria-label="Backyard pool framed by trees and mountains" style="background:linear-gradient(180deg,#dfe7ec 0%,#6d8a6a 35%,var(--water) 65%,#c7b59c 100%)"></div>
      <div class="photo" role="img" aria-label="Blue pool with potted plants on a stone deck" style="background:linear-gradient(170deg,#5d7a4d 0%,#c6a982 35%,var(--water) 70%,var(--water-deep) 100%)"></div>
    </div>
    <div class="logo about-logo">
      <div class="logo-row"><span class="logo-dot"></span><span class="logo-name">tidewellaqua</span></div>
      <span class="logo-tag">Every Wave Stays Bright</span>
    </div>
  </section>

  <section class="panel panel-contact">
    <div class="logo middle-logo">
      <div class="logo-row"><span class="logo-dot"></span><span class="logo-name">tidewellaqua</span></div>
      <span class="logo-tag">Every Wave Stays Bright</span>
    </div>
    <div class="photo mid-small-1" role="img" aria-label="Pool edge with rock waterfall" style="background:linear-gradient(170deg,#7a8c6e 0%,var(--stone) 35%,var(--water) 70%,var(--water-deep) 100%)"></div>
    <div class="photo mid-small-2" role="img" aria-label="Stacked stone water feature spilling into a pool" style="background:linear-gradient(180deg,#8a7a66 0%,#a89274 45%,var(--water) 80%,var(--water-deep) 100%)"></div>
    <div class="photo mid-feature" role="img" aria-label="Rock grotto pool with palm trees at dusk" style="background:linear-gradient(180deg,#4a5a8a 0%,#6f7fa0 30%,#8f8a86 55%,#3d6f8a 100%)">
      <div class="feature-text">
        <div class="headline">Economical<br>&amp; Professional</div>
        <div class="sub">Making your pool special</div>
      </div>
    </div>
    <h2 class="tab contact-tab">Contact Us – 24/7</h2>
    <ul class="contact-list">
      <li><svg width="12" height="12" viewBox="0 0 12 12"><path d="M3 1l2 2.5-1.2 1.2a7 7 0 003.5 3.5L8.5 7 11 9l-1 2C5 11 1 7 1 2z" fill="#3176b5"/></svg>480-555-0147</li>
      <li><svg width="12" height="12" viewBox="0 0 12 12"><circle cx="6" cy="6" r="5" fill="none" stroke="#3176b5"/><path d="M1 6h10M6 1c2 2 2 8 0 10M6 1c-2 2-2 8 0 10" fill="none" stroke="#3176b5" stroke-width=".8"/></svg>www.tidewellaqua.com</li>
      <li><svg width="12" height="12" viewBox="0 0 12 12"><rect x="1" y="1" width="10" height="10" rx="2" fill="#3176b5"/></svg>tidewellaqua</li>
      <li><svg width="12" height="12" viewBox="0 0 12 12"><rect x="1" y="1" width="10" height="10" rx="2" fill="#0355a3"/></svg>+tidewellaqua</li>
    </ul>
    <div class="partners">
      <span class="badge badge-wide" role="img" aria-label="Utility partner badge"></span>
      <span class="badge badge-square" role="img" aria-label="Medical center partner badge"></span>
      <span class="badge badge-round" role="img" aria-label="Utility partner badge"></span>
    </div>
    <address class="address">Office / Warehouse Location<br>41762 East Kettle Lane, Suite 7<br>Phoenix, Arizona 85000<br>(NW of Kettle Lane &amp; Mesquite Ridge Drive)</address>
  </section>

  <section class="panel panel-cover">
    <p class="cover-intro">Providing swimming pool service,<br>repair, and custom renovations<br>throughout the Phoenix, Arizona metropolitan area</p>
    <div class="photo cover-photo" role="img" aria-label="Turquoise pool with boulder waterfall and palms" style="background:linear-gradient(175deg,#6d8d5f 0%,#a68f76 35%,var(--water) 65%,#2b8fa6 100%)"></div>
    <ul class="services">
      <li>Service</li>
      <li>Repair</li>
      <li>Renovation</li>
    </ul>
    <div class="logo cover-logo">
      <div class="logo-row"><span class="logo-dot"></span><span class="logo-name">tidewellaqua</span></div>
      <span class="logo-tag">Every Wave Stays Bright</span>
    </div>
  </section>

</main>
</body>
</html>
```